Fruity, Italy, Healthy Foods for thoughts.

We need a sign board design of a new Restaurant. Its name “Melonetta Restaurant” and Arabic name “مطعم بيرامولا”. Although both names have to be appeared in signage in front of the shop but its ok you cannot do the Arabic one and make the design in English. Its Concept is; Fruits & Italian foods (means: fresh Juices, fruit salads, Pasta, Pizza and Veg. Salads), I've attached a typical design with actual measurements for your reference. I appreciate your creativity on the design as it will be applicable in future branches.

Reason: I have received only few designers (3 to 4) and only one having little acceptability but that no I want, and I have committed my payment I was expected more than 50 designers according to your message but unfortunately it's not happening please for you assistance.

All level of audience

Shop

• Juicy fruity
• Juices fruits pasta pizza

```html
<!DOCTYPE html>
<html lang="en">
<head>
<meta charset="utf-8">
<title>Melonetta Restaurant – Sign Board</title>
<link rel="stylesheet" href="https://fonts.googleapis.com/css2?family=Baloo+2:wght@700&family=Baloo+Bhaijaan+2:wght@700&display=swap">
<style>
  :root {
    --brand-blue: #1c6cc6;
    --accent-orange: #f2661b;
    --wash-green: #3fae2e;
    --wash-lime: #9fcf2a;
    --wash-yellow: #d7e02a;
    --page-bg: #ffffff;
  }
  html, body {
    margin: 0;
    padding: 0;
    width: 1200px;
    height: 139px;
    overflow: hidden;
    background: var(--page-bg);
  }
  .signboard {
    position: relative;
    width: 1200px;
    height: 139px;
    overflow: hidden;
  }
  .signboard__wash {
    position: absolute;
    inset: 0;
    background:
      radial-gradient(ellipse 30% 90% at 48% 45%, var(--wash-yellow) 0%, transparent 70%),
      radial-gradient(ellipse 25% 80% at 85% 60%, var(--wash-lime) 0%, transparent 75%),
      linear-gradient(90deg, var(--wash-green) 0%, var(--wash-lime) 25%, var(--wash-yellow) 45%, var(--wash-lime) 65%, var(--wash-green) 100%);
  }
  .name-latin {
    position: absolute;
    left: 46px;
    top: 2px;
    width: 520px;
    text-align: center;
    font-family: "Baloo 2", sans-serif;
    font-weight: 700;
  }
  .name-latin__title {
    display: block;
    color: var(--brand-blue);
    font-size: 88px;
    line-height: 88px;
    letter-spacing: 0.5px;
  }
  .name-latin__subtitle {
    display: block;
    margin-top: -6px;
    color: var(--accent-orange);
    font-size: 30px;
    line-height: 32px;
  }
  .name-arabic {
    position: absolute;
    right: 52px;
    top: 0;
    width: 470px;
    text-align: center;
    font-family: "Baloo Bhaijaan 2", sans-serif;
    font-weight: 700;
    direction: rtl;
  }
  .name-arabic__label {
    display: block;
    color: var(--accent-orange);
    font-size: 40px;
    line-height: 44px;
    padding-left: 120px;
  }
  .name-arabic__title {
    display: block;
    margin-top: -10px;
    color: var(--brand-blue);
    font-size: 92px;
    line-height: 96px;
  }
</style>
</head>
<body>
  <div class="signboard">
    <div class="signboard__wash" role="img" aria-label="Green and yellow watercolour wash background"></div>

    <div class="name-latin">
      <span class="name-latin__title">Melonetta</span>
      <span class="name-latin__subtitle">Restaurant</span>
    </div>

    <div class="name-arabic" lang="ar">
      <span class="name-arabic__label">مطعم</span>
      <span class="name-arabic__title">بـيـرامـولا</span>
    </div>
  </div>
</body>
</html>
```